self-employed education content specialist/consultant needs business card and logo design

I need a design for a double-sided business card (and logo) for my nascent consultancy business based in London UK, to hand out at a London trade show in a couple of weeks. The business simply has my name, "Marcus Tenwold".

I describe my service as a "content and engagement consultant". In essence I cover 2 areas:
- Advice to organisations on effective strategies and tactics for creating and distributing large volumes of media-rich content (video and interactive) for learning, training and professional development, that successfully engages and impacts on students and their teachers.
- Advice on growing and maintaining customer/end-user engagement to help maximise the reach and usage of this content.

I have uploaded a weighted list of key words that offer I hope a good feel of "the brand".

In terms of design I have put together a very rough initial idea for the card (see attached doc), which gives an idea of the key messages in text, but I feel it is not working visually, and looks too amateur. In particular I think the background/visuals of the info side needs work; the word cloud on the back of the card is perhaps rather "passé" and could be improved on; there is no "logo" at present; and I think overall it's not very "creative", i.e. it doesn't "stand out".

I am not set on font or background colours/design. The font itself should not be too businessy or too "comic sans", hence I've currently gone for something like Odile or Playfair Display.

Also note that
1. given budget and time constraints, I'm looking for designs for printing on paper, and to be of a fairly standard business card shape/size.
2. I have no web address at present, but will need a card design that can cope with this being added at a later date.

Overall I am hoping for something fairly clean, simple and clear, that will impress and speak to senior managers/business owners working in the education and edtech sectors.

As a self-employed consultant my budget is limited, so I don't expect the world for what I can offer, but am hoping that there are design experts out there who can swiftly interpret my brief and produce something suitable for my needs.

Target Market(s)

senior managers/business owners working in the education and edtech sectors.

Contact Information for Business Card

marcus tenwold
content and engagement consultant
education - training - development
+44 (0) 7731 482905
marcus.tenwold@quorvane.com

Font styles to use
Other font styles liked:
• Odile or Playfair Display are my favourites for now.

Colors

Designer to choose colors to be used in the design.

```html
<!DOCTYPE html>
<html lang="en">
<head>
<meta charset="utf-8">
<title>Marcus Tenwold – Business Card</title>
<link href="https://fonts.googleapis.com/css2?family=Playfair+Display:ital,wght@0,400;0,500;1,400&display=swap" rel="stylesheet">
<style>
  :root {
    --paper: #ffffff;
    --card: #2d2d2d;
    --gold: #c98a40;
  }
  * { margin: 0; padding: 0; box-sizing: border-box; }
  html, body {
    width: 898px;
    height: 1200px;
    overflow: hidden;
    background: var(--paper);
  }
  body {
    position: relative;
    font-family: "Playfair Display", Georgia, serif;
    color: var(--gold);
  }
  .card {
    position: absolute;
    left: 25px;
    width: 848px;
    height: 548px;
    background: var(--card);
  }
  .card--front { top: 34px; }
  .card--back { top: 618px; }

  .brand-mark {
    position: absolute;
    top: 198px;
    left: 0;
    width: 100%;
    text-align: center;
    font-size: 30px;
    font-weight: 400;
    line-height: 1;
  }
  .front-name {
    position: absolute;
    top: 341px;
    left: 0;
    width: 100%;
    text-align: center;
    font-size: 40px;
    font-weight: 400;
    letter-spacing: 0.3em;
    padding-left: 0.3em;
    text-transform: uppercase;
    line-height: 1;
  }

  .identity {
    position: absolute;
    right: 81px;
    top: 142px;
    text-align: right;
  }
  .identity__name {
    font-size: 37px;
    font-weight: 400;
    text-transform: uppercase;
    line-height: 1;
  }
  .identity__role,
  .identity__areas {
    font-style: italic;
    font-size: 23px;
    line-height: 1;
  }
  .identity__role { margin-top: 26px; }
  .identity__areas { margin-top: 24px; }

  .contact {
    position: absolute;
    left: 85px;
    top: 400px;
    font-size: 22px;
    line-height: 30px;
  }
</style>
</head>
<body>
  <section class="card card--front">
    <div class="brand-mark">Marcus Tenwold</div>
    <h1 class="front-name">Marcus Tenwold</h1>
  </section>

  <section class="card card--back">
    <div class="identity">
      <h2 class="identity__name">Marcus Tenwold</h2>
      <p class="identity__role">Content And Engagement Consultant</p>
      <p class="identity__areas">education – training – development</p>
    </div>
    <div class="contact">
      <p class="contact__phone">+44 (0) 7731 482905</p>
      <p class="contact__email">marcus.tenwold@quorvane.com</p>
    </div>
  </section>
</body>
</html>
```